Magazine Design Project

Our company Villa Sorbetto Nero - www.villasorbettonero.co.uk

Villa Sorbetto Nero has been established for three years and produce artisan gelato from fresh ingredients on a wholesale scale. We also cater for weddings and parties.
We supply in scoop cups, ready to scoop pans and can arrange a display freezer of 10 flavours with staff to scoop for guests.

We need a A4 full spread Magazine Advertisement (with 5mm border from the edge of the page) for a Gelato wholesaling business. It'll be advertised in a local community Indian arts magazine so needs to be eyecatching with colourful images boasting handmade artisan gelato. Most readers of this magazine will be of indian origin and self employed business owners looking for new ideas and oppurtunities and will be viewing events and productions organised by the arts company.

We pride ourselves with our inventive flavours and exceptional prices.

We would like to see designs showing colourful pans of gelato, details of what we sell and still maintaining an image of premium, quality and an authentic italian product.

Target Market(s)

Ages 20-60, Male & Female, All education levels, Self Employed who are looking to introduce this product in their food business,

Industry/Entity Type

Events

Requirements
Must have
• The design must be one A4 page and use the logo on the first page of the document we have attached - the border around the logo can be ommitted as we have done on our website www.villasorbettonero.co.uk
Nice to have
• Bold colours, artisan gelato images and an authentic Italian feel
Should not have
• Should not look like it appeals to children or have images of standard ice cream cones. Avoid putting cost list on the advertisement

```html
<!DOCTYPE html>
<html lang="en">
<head>
<meta charset="utf-8">
<title>Villa Sorbetto Nero – The House of Italian Ice Cream</title>
<link href="https://fonts.googleapis.com/css2?family=Almendra&family=Arimo&family=Patrick+Hand+SC&display=swap" rel="stylesheet">
<style>
  :root {
    --paper: #ffffff;
    --brown: #6e4b3a;
    --body-text: #4f4440;
    --pink: #e0338f;
    --teal: #2db6aa;
    --green: #a8c540;
    --coral: #ee6e5c;
    --stitch: rgba(255,255,255,0.85);
    --photo-light: #fbf6ef;
    --photo-warm: #f5c77a;
  }
  * { margin: 0; padding: 0; box-sizing: border-box; }
  html, body { width: 848px; height: 1200px; overflow: hidden; background: var(--paper); }
  .page { position: relative; width: 848px; height: 1200px; overflow: hidden; background: var(--paper); }

  .brand-mark {
    position: absolute; top: 72px; left: 565px; width: 86px; height: 86px;
    border: 2px solid var(--brown); border-radius: 50%;
  }
  .brand-name {
    position: absolute; top: 214px; left: 395px; width: 425px; text-align: center;
    font-family: 'Almendra', serif; font-size: 50px; color: var(--brown);
    line-height: 1; white-space: nowrap;
  }
  .tagline {
    position: absolute; top: 308px; left: 430px; width: 360px; text-align: center;
    font-family: 'Almendra', serif; font-size: 25px; color: var(--brown);
  }

  .hero-photo {
    position: absolute; left: 0; top: 250px; width: 460px; height: 420px;
    background: linear-gradient(160deg, var(--photo-light) 0%, var(--photo-warm) 100%);
  }

  .menu { position: absolute; left: 440px; width: 360px; text-align: center; color: var(--body-text); }
  .menu-gelato { top: 375px; }
  .menu-sorbetto { top: 769px; }
  .menu-heading {
    font-family: 'Patrick Hand SC', cursive; color: var(--pink);
    font-size: 14px; line-height: 14px; margin-bottom: 1px; font-weight: normal;
  }
  .menu-list { font-family: 'Arimo', sans-serif; font-size: 13.4px; line-height: 17.2px; white-space: nowrap; }

  .waves { position: absolute; left: 0; top: 0; width: 848px; height: 1200px; }
</style>
</head>
<body>
<main class="page">
  <div class="brand-mark"></div>
  <h1 class="brand-name">Villa Sorbetto Nero</h1>
  <p class="tagline">The House of Italian Ice Cream</p>

  <div class="hero-photo" role="img" aria-label="Photograph of a scoop of mango gelato on a white spoon, garnished with a raspberry and mint leaves"></div>

  <section class="menu menu-gelato">
    <h2 class="menu-heading">Gelato</h2>
    <p class="menu-list">Fior De Latte • Vanilla • Chocolate<br>
• Mint Chocolate Chip • Strawberry• Stracciatella<br>
(Chocolate Chip) • Dulce De Leche (Caramel) •<br>
Salted Caramel • Rum &amp; Raisin • Cherry Ripple •<br>
Cherry Yoghurt • Raspberry Ripple • Strawberry<br>
Ripple • Lime Ripple • Hazelnut • Donatella<br>
(Chocolate &amp; Hazelnut/ Nocciola Dorata) • Pistachio<br>
(Pure Sicilian) • Tiramisu • Banana • Banoffee •<br>
Strawberry Cheesecake • Biscotti Cookie • Ombra<br>
Cookie • Chocolate Fudge Brownie • White<br>
Chocolate • Coconut • Coconut &amp; Chocolate<br>
(Isola) • Toffee • Peanut • Chocolate Chip Cookie<br>
Dough • Chocolate, Peanut &amp; Caramel (Arachide) •<br>
Chocolate Orange • Chilli Chocolate • Lemon Cream<br>
• Cappuccino • Salty Peanut • Cinnamon •<br>
Bubblegum (Pink) • Bubblegum (Blue) • Saffron,<br>
Apricot &amp; Almond• Rose Petal • Honeycomb &amp;<br>
Chocolate (Favo Bar) • Faluda (with Tapioca Seeds)<br>
• Fusion (Villa's special blend of rose, saffron,<br>
cardomom, rippled with figs and vegetarian fruit<br>
jellies) • Mango - Alphonso</p>
  </section>

  <section class="menu menu-sorbetto">
    <h2 class="menu-heading">Sorbetto</h2>
    <p class="menu-list">Exotic Tropical Fruits • Pineapple • Raspberry •<br>
Strawberry • Orange • Passion Fruit • Mango •<br>
Melon • Lemon • Champagne</p>
  </section>

  <svg class="waves" viewBox="0 0 848 1200" aria-hidden="true">
    <path class="wave wave-teal" fill="var(--teal)" d="M0,655 C130,700 290,760 420,830 C550,900 660,1010 745,1200 L0,1200 Z"/>
    <path class="stitch" fill="none" stroke="var(--stitch)" stroke-width="2.5" stroke-dasharray="12 8" d="M0,680 C130,725 285,785 410,852 C540,922 640,1025 718,1200"/>
    <path class="wave wave-green" fill="var(--green)" d="M0,850 C200,830 390,880 505,960 C600,1030 660,1120 705,1200 L0,1200 Z"/>
    <path class="stitch" fill="none" stroke="var(--stitch)" stroke-width="2.5" stroke-dasharray="12 8" d="M0,872 C195,853 380,902 490,980 C580,1048 635,1130 678,1200"/>
    <path class="wave wave-coral" fill="var(--coral)" d="M0,1098 C150,1082 330,1118 440,1150 C480,1163 510,1183 528,1200 L0,1200 Z"/>
    <path class="stitch" fill="none" stroke="var(--stitch)" stroke-width="2.5" stroke-dasharray="12 8" d="M0,1118 C150,1103 325,1138 430,1168 C458,1177 480,1188 495,1200"/>
  </svg>
</main>
</body>
</html>
```